new KVR one page flyer

We need a 1 page A4 size flyer (need it asap please) that describes on 1 page with art work and using photos the services we provide. I have included some examples of old previous flyers from our other (seperate divisions of the business) I have named a photo called (photo for top of design) however you do your design this photo needs to be the star of the page by either having it at the top or bottom of the page please and we usually like this photo to be in greyscale colour.
we do like greyscale designs but are open to see what you come up with as a whole page of grey white and black might not suit.

Needs to list the following

Services include:
Over size loads / Hot Shot Loads
Heavy Vehicle Recovery services
Potable Water Deliveries
Road Building / Maintenance
Earthworks
Sand & Metal Supply & Cartage
Road Train Tippers
Road Train Tankers
Road Train Flat Tops
Drop Deck Trailers
Mine site accredited equipment & Operators.

We offer a large rage of services not listed so call us today for a personalised quote to suit your needs.

To go on the bottom of the page our contact details are

KVR Pty Ltd
Depot: Lot 514, Banksia Flats Track Coober Pedy
Mobile: 047 216 9381
email: darren@kestrelvaleroadworks.com.au

Target Market(s)

new clients

Colors

Designer to choose colors to be used in the design.

Requirements
Must have
• our services listed
Nice to have
• stand out designs

```html
<!DOCTYPE html>
<html lang="en">
<head>
<meta charset="utf-8">
<title>KVR Services Flyer</title>
<link href="https://fonts.googleapis.com/css2?family=Bebas+Neue&family=Roboto:wght@400;500;700&display=swap" rel="stylesheet">
<style>
  :root {
    --bg: #d4d4d4;
    --paper: #ffffff;
    --dark: #232323;
    --darker: #1b1b1b;
    --yellow: #f7b500;
    --ink: #222222;
    --white: #ffffff;
  }
  * { box-sizing: border-box; margin: 0; padding: 0; }
  html, body { width: 1200px; height: 1200px; overflow: hidden; background: var(--bg); }
  .flyer {
    position: absolute; left: 172px; top: 0;
    width: 925px; height: 1297px;
    background: var(--paper);
    transform: scale(0.925); transform-origin: 0 0;
    font-family: "Roboto", Arial, sans-serif;
    overflow: hidden;
  }
  .photo { position: absolute; }
  .hero-photo {
    left: 330px; top: 62px; width: 595px; height: 473px;
    background: linear-gradient(180deg, #7d8188 0%, #9a9ea5 40%, #8a6a55 62%, #a0694a 100%);
  }
  .hero-panel { position: absolute; left: 0; top: 0; width: 540px; height: 580px; }
  .hero-rule { position: absolute; left: 575px; top: 553px; width: 350px; height: 7px; background: var(--dark); }
  .brand {
    position: absolute; left: 52px; top: 96px;
    font-family: "Bebas Neue", sans-serif; font-size: 104px; line-height: 1;
    color: #c9c9c9; letter-spacing: 4px;
  }
  .offer-tag {
    position: absolute; left: 55px; top: 222px; width: 293px; height: 54px;
    background: var(--white);
    font-size: 50px; line-height: 56px; color: #111; padding-left: 6px; letter-spacing: -0.5px;
  }
  .headline {
    position: absolute; left: 60px; top: 272px;
    font-family: "Bebas Neue", sans-serif; font-size: 113px; line-height: 90px;
    color: var(--yellow); letter-spacing: 1px;
  }
  .services-title {
    position: absolute; left: 60px; top: 630px;
    font-family: "Bebas Neue", sans-serif; font-size: 42px; line-height: 40px; color: var(--ink);
    padding-left: 16px;
  }
  .services-title::before {
    content: ""; position: absolute; left: 0; top: 4px; width: 6px; height: 30px;
    background: linear-gradient(180deg, var(--yellow) 50%, var(--ink) 50%);
  }
  .services-title .accent { color: var(--yellow); }
  .service-list { position: absolute; left: 62px; top: 692px; list-style: none; }
  .service-list li {
    position: relative; padding-left: 20px;
    font-size: 18px; line-height: 27.2px; color: var(--ink);
  }
  .service-list li::before {
    content: ""; position: absolute; left: 0; top: 9px; width: 10px; height: 10px;
    border-radius: 50%; background: var(--yellow);
  }
  .service-list li .wrap { display: block; line-height: 20px; }
  .bottom-photo {
    left: 0; top: 1003px; width: 458px; height: 200px;
    background: linear-gradient(180deg, #ffffff 0%, #dfe8f0 25%, #9bb2c4 60%, #8a7463 100%);
  }
  .ph-main { left: 462px; top: 600px; width: 444px; height: 240px; background: linear-gradient(180deg, #4c86d6 0%, #8db6e6 50%, #8e5a3e 80%, #a06a4a 100%); }
  .ph-a { left: 462px; top: 845px; width: 194px; height: 120px; background: linear-gradient(180deg, #c8ccd2 0%, #a5a8ad 50%, #a9704e 100%); }
  .ph-b { left: 660px; top: 845px; width: 246px; height: 172px; background: linear-gradient(180deg, #b9bec6 0%, #9aa0a6 50%, #b07a58 100%); }
  .ph-c { left: 462px; top: 968px; width: 194px; height: 234px; background: linear-gradient(180deg, #5b8fd4 0%, #c9d6e4 35%, #a0653f 70%, #c58456 100%); }
  .ph-d { left: 660px; top: 1021px; width: 246px; height: 181px; background: linear-gradient(180deg, #4b7fcf 0%, #a9c1dd 40%, #8c5a3e 75%, #a36a48 100%); }
  .footer {
    position: absolute; left: 0; top: 1208px; width: 925px; height: 89px;
    background: var(--darker); color: var(--white); font-size: 16px;
  }
  .contact { position: absolute; display: flex; align-items: center; gap: 10px; line-height: 20px; }
  .contact svg { flex: none; }
  .contact-depot { left: 38px; top: 22px; }
  .contact-email { left: 383px; top: 24px; }
  .contact-phone { left: 730px; top: 24px; }
</style>
</head>
<body>
<div class="flyer">
  <div class="photo hero-photo" role="img" aria-label="Road train tipper truck on red dirt under a cloudy outback sky, shown in greyscale"></div>

  <svg class="hero-panel" viewBox="0 0 540 580" aria-hidden="true">
    <polygon points="0,0 328,0 536,579 0,579" fill="#232323"/>
  </svg>
  <div class="hero-rule"></div>

  <div class="brand">KVR</div>
  <div class="offer-tag">WE OFFER</div>
  <h1 class="headline">A LARGE<br>RAGE OF<br>SERVICES</h1>

  <h2 class="services-title"><span class="accent">SERVICES</span> INCLUDE</h2>
  <ul class="service-list">
    <li>Over size loads / Hot Shot Loads</li>
    <li>Heavy Vehicle Recovery services</li>
    <li>Potable Water Deliveries</li>
    <li>Road Building / Maintenance</li>
    <li>Earthworks</li>
    <li>Sand &amp; Metal Supply &amp; Cartage</li>
    <li>Road Train Tippers</li>
    <li>Road Train Tankers</li>
    <li>Road Train Flat Tops</li>
    <li>Drop Deck Trailers</li>
    <li><span class="wrap">Mine site accredited equipment<br>&amp; Operators.</span></li>
  </ul>

  <div class="photo bottom-photo" role="img" aria-label="Truck hauling a relocated building along a town road"></div>
  <div class="photo ph-main" role="img" aria-label="Black prime mover pulling water tanker trailers"></div>
  <div class="photo ph-a" role="img" aria-label="Truck carrying site accommodation buildings"></div>
  <div class="photo ph-b" role="img" aria-label="Loaders carried on a drop deck trailer"></div>
  <div class="photo ph-c" role="img" aria-label="Oversize tank load on a truck in the desert"></div>
  <div class="photo ph-d" role="img" aria-label="Trucks parked at the depot yard"></div>

  <footer class="footer">
    <div class="contact contact-depot">
      <svg width="34" height="36" viewBox="0 0 34 36" aria-hidden="true">
        <ellipse cx="17" cy="30" rx="15" ry="5" fill="none" stroke="#f7b500" stroke-width="2.5"/>
        <path d="M17 31 C10 22 8 18 8 13 a9 9 0 0 1 18 0 c0 5 -2 9 -9 18z" fill="#f7b500"/>
        <circle cx="17" cy="13" r="3.5" fill="#1b1b1b"/>
      </svg>
      <span>Depot: Lot 514,<br>Banksia Flats Track Coober Pedy</span>
    </div>
    <div class="contact contact-email">
      <svg width="30" height="18" viewBox="0 0 30 18" aria-hidden="true">
        <rect x="1" y="1" width="28" height="16" fill="none" stroke="#f7b500" stroke-width="2"/>
        <polyline points="1,1 15,11 29,1" fill="none" stroke="#f7b500" stroke-width="2"/>
      </svg>
      <span>darren@kestrelvaleroadworks.com.au</span>
    </div>
    <div class="contact contact-phone">
      <svg width="20" height="36" viewBox="0 0 20 36" aria-hidden="true">
        <path d="M6 2 l5 -1 3 9 -4 2 c-1 4 -1 8 0 12 l4 2 -3 9 -5 -1 C0 26 0 10 6 2z" fill="#f7b500"/>
      </svg>
      <span>047 216 9381</span>
    </div>
  </footer>
</div>
</body>
</html>
```